Security company needs HTML and CSS files and templates made & Blogs

need HTML files and template pages created for about us, staff, MMJ transport, vehicles, alarm systems, video systems, gaurd services, private investigations, surveillance audit request form, and compliance investigation request form, blog setup for video systems, alarm systems, and video monitoring. Needs to be Adobe Dreamweaver CS6 Format. Website needs to be based off the original PSD file. All images must be original or royalty free for use.

Target Market(s)

Customers

Industry/Entity Type

Security

Coding

Coded - Design and coding required

Number of Pages Required

5+ page

Requirements
Must have
• template pages created for about us, staff, MMJ transport, vehicles, alarm systems, video systems, gaurd services, private investigations, surveillance audit request form, and compliance investigation request form, blog setup for video systems, alarm systems, and video monitoring. Needs to be Adobe Dreamweaver CS6 Format Website needs to be based off the original PSD file
Nice to have
• Scheduling calendar built in that interfaces with Microsoft Exchange, Blogs

```html
<!DOCTYPE html>
<html lang="en">
<head>
<meta charset="utf-8">
<title>Guardline – Enforcement Solutions</title>
<link href="https://fonts.googleapis.com/css2?family=Roboto:ital,wght@0,300;0,400;0,500;0,700;0,900;1,700;1,900&display=swap" rel="stylesheet">
<style>
:root{
  --blue:#1b8fd6;
  --blue-dark:#0d5c9c;
  --navy:#0b3f6e;
  --green:#8cc63f;
  --green-dark:#6fa82a;
  --red:#d7262d;
  --ink:#333a40;
  --muted:#7b838a;
  --line:#e2e6ea;
  --paper:#ffffff;
}
*{box-sizing:border-box;margin:0;padding:0}
html,body{width:1200px;height:2620px;overflow:hidden}
body{font-family:"Roboto",Arial,sans-serif;color:var(--ink);background:var(--paper);font-size:13px;line-height:1.55}
.wrap{width:960px;margin:0 auto;position:relative}
a{color:inherit;text-decoration:none}

/* top bar */
.topbar{height:40px;position:relative}
.topbar .contact-tab{position:absolute;right:0;top:0;height:32px;width:340px;background:var(--blue);color:#fff;font-size:12px;display:flex;align-items:center;justify-content:center;gap:26px;border-bottom-left-radius:14px}
.contact-tab span{display:flex;align-items:center;gap:6px}

/* header */
.header{height:120px}
.header .wrap{display:flex;justify-content:space-between;align-items:center;height:100%}
.brand{display:flex;align-items:center;gap:10px;font-size:26px;font-weight:700;color:var(--blue-dark)}
.brand .dot{width:34px;height:34px;border-radius:50%;background:var(--red)}
.top-links{display:flex;gap:34px;font-size:13px;color:var(--ink)}

/* main nav */
.mainnav{height:40px;background:var(--green)}
.mainnav ul{list-style:none;display:flex;height:40px;align-items:stretch}
.mainnav li{color:#fff;font-size:12.5px;padding:0 17px;display:flex;align-items:center}
.mainnav li.active{background:var(--green-dark)}

/* hero */
.hero{height:520px;position:relative;background:linear-gradient(160deg,#0c2340 0%,#123b63 45%,#1f5f8e 70%,#0a1a30 100%);overflow:hidden}
.hero .copy{position:absolute;left:120px;top:150px;color:#fff}
.hero h1{font-size:44px;font-weight:700;line-height:1.15;font-style:italic}
.hero p{font-size:15px;margin:14px 0 28px}
.btn{display:inline-block;background:var(--blue);color:#fff;font-size:13px;padding:9px 22px;border-radius:3px}
.hero .arrow{position:absolute;top:240px;width:20px;height:40px}
.hero .arrow.left{left:30px}
.hero .arrow.right{right:30px}

/* services band */
.services{height:220px;background:linear-gradient(100deg,var(--blue) 0%,var(--blue) 49%,var(--green) 49.2%,var(--green) 100%);color:#fff}
.services .wrap{display:flex;height:100%}
.service{flex:1;display:flex;align-items:center;gap:22px;padding:0 30px}
.service h3{font-size:21px;font-weight:500;text-transform:uppercase;margin-bottom:6px}
.service p{font-size:11px;opacity:.9;max-width:300px}

/* about */
.about{height:480px;text-align:center;position:relative}
.emblem{width:40px;height:40px;border-radius:50%;background:var(--red);margin:0 auto;position:relative;top:-18px}
.section-title{font-size:28px;font-weight:900;color:var(--ink);text-transform:uppercase;margin-top:4px}
.section-title em{color:var(--red);font-style:italic}
.section-sub{font-size:11px;letter-spacing:1px;color:var(--muted);text-transform:uppercase;margin-top:4px;position:relative;padding-bottom:12px}
.section-sub::after{content:"";position:absolute;left:50%;bottom:0;width:60px;height:2px;margin-left:-30px;background:var(--red)}
.features{display:flex;justify-content:space-between;margin-top:40px}
.feature{width:220px}
.feature svg{display:block;margin:0 auto 14px}
.feature h4{font-size:16px;font-weight:500;margin-bottom:6px}
.feature p{font-size:11px;color:var(--muted);line-height:1.6}
.more{display:inline-block;font-size:11px;color:var(--blue-dark);font-weight:500;margin-top:10px}

/* request band */
.requests{height:290px;background:linear-gradient(100deg,var(--blue) 0%,var(--blue) 49.5%,var(--green) 49.7%,var(--green) 100%);color:#fff;position:relative}
.requests .wrap{display:flex;height:100%;align-items:center}
.request{flex:1;padding:0 90px 0 10px}
.request + .request{padding:0 10px 0 100px}
.request h3{font-size:26px;font-weight:400;margin-bottom:8px}
.request p{font-size:11px;opacity:.9;margin-bottom:18px}
.btn-outline{display:inline-block;border:1px solid #fff;color:#fff;font-size:12px;padding:7px 22px;border-radius:3px}
.requests .seal{position:absolute;left:50%;top:50%;width:120px;height:120px;margin:-60px 0 0 -60px;border-radius:50%;background:#ffffff;border:6px solid var(--navy)}

/* blog */
.blog{height:530px;text-align:center;padding-top:36px}
.posts{display:flex;justify-content:space-between;margin-top:32px;text-align:left}
.post{width:300px;border:1px solid var(--line);background:#fff;height:360px;display:flex;flex-direction:column}
.post .thumb{height:160px}
.post .body{padding:16px 18px;flex:1;display:flex;flex-direction:column}
.post h4{font-size:17px;font-weight:500;margin-bottom:8px}
.post p{font-size:11px;color:var(--muted);line-height:1.6;flex:1}
.post .date{font-size:11px;color:var(--ink);border-top:1px solid var(--line);padding-top:8px}
.thumb.alarm{background:linear-gradient(135deg,#c9d3dc,#8795a3)}
.thumb.video{background:linear-gradient(135deg,#e7a46b,#46617d)}
.thumb.monitor{background:linear-gradient(135deg,#1d4a7a,#7db0d8)}

/* footer */
.footer{height:310px;background:var(--navy);color:#cfe0ef}
.footer .wrap{display:flex;padding-top:50px;gap:40px}
.footer h5{color:#fff;font-size:14px;font-weight:500;text-transform:uppercase;margin-bottom:16px}
.col-badge{width:200px}
.badge{width:120px;height:120px;border-radius:50%;background:#c9a23b;border:5px solid #0a2d52;margin-bottom:18px}
.socials{display:flex;gap:8px}
.socials span{width:26px;height:26px;border-radius:50%;border:1px solid #cfe0ef}
.col-links{width:150px}
.col-links ul{list-style:none;font-size:12px;line-height:2}
.col-contact{width:240px;font-size:12px}
.col-contact li{list-style:none;display:flex;gap:8px;margin-bottom:10px}
.col-form{flex:1}
.form-row{display:flex;gap:8px;margin-bottom:8px}
.field{flex:1;height:28px;background:#fff;border-radius:2px;font-size:11px;color:#999;padding:6px 8px}
.field.area{height:70px}
.submit{display:inline-block;background:var(--green);color:#fff;font-size:11px;padding:6px 16px;border-radius:2px;text-transform:uppercase}

/* bottom */
.bottom{height:70px;background:var(--green);color:#fff;font-size:11px}
.bottom .wrap{height:100%;display:flex;align-items:center}
</style>
</head>
<body>

<div class="topbar">
  <div class="contact-tab">
    <span><svg width="12" height="10" viewBox="0 0 12 10"><rect x="0.5" y="0.5" width="11" height="9" fill="none" stroke="#fff"/><path d="M0.5 0.5 6 5 11.5 0.5" fill="none" stroke="#fff"/></svg>info@guardline.example</span>
    <span><svg width="10" height="12" viewBox="0 0 10 12"><rect x="1" y="0.5" width="8" height="11" rx="1.5" fill="none" stroke="#fff"/></svg>1 800 555 0142</span>
  </div>
</div>

<header class="header">
  <div class="wrap">
    <a class="brand" href="#"><span class="dot"></span>Guardline</a>
    <nav class="top-links">
      <a href="#">Private Investigations</a>
      <a href="#">Surveillance Audit</a>
      <a href="#">Compliance Investigations</a>
      <a href="#">Contact Us</a>
    </nav>
  </div>
</header>

<nav class="mainnav">
  <div class="wrap">
    <ul>
      <li class="active">Home</li>
      <li>About Us</li>
      <li>Our Staff</li>
      <li>Cargo Transport &amp; Courier Services</li>
      <li>Our Vehicles</li>
      <li>Alarm Systems</li>
      <li>Video Systems</li>
    </ul>
  </div>
</nav>

<section class="hero" role="img" aria-label="Security camera on a wall overlooking a city skyline at night">
  <svg class="arrow left" viewBox="0 0 20 40"><path d="M16 4 4 20 16 36" fill="none" stroke="#fff" stroke-width="3"/></svg>
  <div class="copy">
    <h1>Guardline Enforcement<br>Solutions</h1>
    <p>We are a trusted local security services company.</p>
    <a class="btn" href="#">Read More</a>
  </div>
  <svg class="arrow right" viewBox="0 0 20 40"><path d="M4 4 16 20 4 36" fill="none" stroke="#fff" stroke-width="3"/></svg>
</section>

<section class="services">
  <div class="wrap">
    <div class="service">
      <svg width="110" height="50" viewBox="0 0 110 50" fill="#fff"><rect x="0" y="10" width="30" height="28" rx="3"/><rect x="38" y="6" width="32" height="32" rx="4"/><rect x="78" y="14" width="32" height="24" rx="3"/><circle cx="8" cy="42" r="5"/><circle cx="24" cy="42" r="5"/><circle cx="46" cy="42" r="5"/><circle cx="62" cy="42" r="5"/><circle cx="86" cy="42" r="5"/><circle cx="102" cy="42" r="5"/></svg>
      <div>
        <h3>Transport Services</h3>
        <p>Secure courier runs and escorted transport handled by trained drivers in tracked vehicles, day or night.</p>
      </div>
    </div>
    <div class="service">
      <svg width="50" height="56" viewBox="0 0 50 56"><path d="M25 2 47 10V26C47 40 37 50 25 54 13 50 3 40 3 26V10Z" fill="none" stroke="#fff" stroke-width="3"/><path d="M15 28 22 35 36 20" fill="none" stroke="#fff" stroke-width="3"/></svg>
      <div>
        <h3>Security Services</h3>
        <p>Licensed guards, alarm response and site patrols built around the needs of each client and property.</p>
      </div>
    </div>
  </div>
</section>

<section class="about">
  <div class="wrap">
    <div class="emblem"></div>
    <h2 class="section-title">About <em>Guardline</em></h2>
    <div class="section-sub">Enforcement Solutions</div>
    <div class="features">
      <div class="feature">
        <svg width="74" height="84" viewBox="0 0 74 84"><path d="M37 2 71 14V40C71 62 55 76 37 82 19 76 3 62 3 40V14Z" fill="var(--blue)"/><path d="M27 50V38a10 10 0 0 1 20 0V50Zm-3 0h26M34 54a3 3 0 0 0 6 0" fill="none" stroke="#fff" stroke-width="3"/></svg>
        <h4>Alarm Systems</h4>
        <p>Monitored alarms for homes and businesses, installed and serviced by our own certified technicians.</p>
        <a class="more" href="#">Read More ›</a>
      </div>
      <div class="feature">
        <svg width="74" height="84" viewBox="0 0 74 84"><path d="M37 2 71 14V40C71 62 55 76 37 82 19 76 3 62 3 40V14Z" fill="var(--red)"/><rect x="22" y="32" width="24" height="18" rx="2" fill="#fff"/><path d="M46 37 54 32V50L46 45Z" fill="#fff"/></svg>
        <h4>Video Systems</h4>
        <p>High definition cameras and recorders that keep a clear record of every entrance and every hour.</p>
        <a class="more" href="#">Read More ›</a>
      </div>
      <div class="feature">
        <svg width="74" height="84" viewBox="0 0 74 84"><path d="M37 2 71 14V40C71 62 55 76 37 82 19 76 3 62 3 40V14Z" fill="var(--blue)"/><rect x="21" y="28" width="32" height="22" rx="2" fill="none" stroke="#fff" stroke-width="3"/><path d="M31 56H43M37 50V56" stroke="#fff" stroke-width="3"/></svg>
        <h4>Video Monitoring</h4>
        <p>Live operators watch your cameras around the clock and respond the moment something looks wrong.</p>
        <a class="more" href="#">Read More ›</a>
      </div>
      <div class="feature">
        <svg width="74" height="84" viewBox="0 0 74 84"><path d="M37 2 71 14V40C71 62 55 76 37 82 19 76 3 62 3 40V14Z" fill="var(--blue)"/><circle cx="34" cy="38" r="9" fill="none" stroke="#fff" stroke-width="3"/><path d="M41 45 50 54" stroke="#fff" stroke-width="4"/></svg>
        <h4>Private Investigations</h4>
        <p>Discreet, licensed investigators for background checks, fraud cases and workplace concerns.</p>
        <a class="more" href="#">Read More ›</a>
      </div>
    </div>
  </div>
</section>

<section class="requests">
  <div class="wrap">
    <div class="request">
      <h3>Surveillance Audit</h3>
      <p>Request a full review of your current cameras, alarms and access points. Our team visits the site, checks coverage and blind spots, and delivers a written report with clear steps to improve protection.</p>
      <a class="btn-outline" href="#">Read More</a>
    </div>
    <div class="request">
      <h3>Compliance Investigations</h3>
      <p>Request an independent compliance investigation. We review records, interview staff and document findings so your business can meet licensing rules and regulatory standards with confidence.</p>
      <a class="btn-outline" href="#">Read More</a>
    </div>
  </div>
  <div class="seal"></div>
</section>

<section class="blog">
  <div class="wrap">
    <h2 class="section-title"><em>Guardline</em> Blog</h2>
    <div class="section-sub">Enforcement Solutions</div>
    <div class="posts">
      <article class="post">
        <div class="thumb alarm" role="img" aria-label="Wall mounted security cameras against a pale sky"></div>
        <div class="body">
          <h4>Alarm Systems</h4>
          <p>How a modern monitored alarm protects your property, what sensors to choose, and how quick response keeps losses low for homes and small businesses.</p>
          <div class="date">Posted 2 days ago »</div>
        </div>
      </article>
      <article class="post">
        <div class="thumb video" role="img" aria-label="City skyline by the water at sunset"></div>
        <div class="body">
          <h4>Video Systems</h4>
          <p>Choosing the right cameras and recorders for your site, from resolution and storage to night vision and remote viewing on your phone.</p>
          <div class="date">Posted 2 days ago »</div>
        </div>
      </article>
      <article class="post">
        <div class="thumb monitor" role="img" aria-label="Hand touching a glowing digital security screen"></div>
        <div class="body">
          <h4>Video Monitoring</h4>
          <p>What live monitoring adds to your camera system and how trained operators verify alerts before calling police or keyholders.</p>
          <div class="date">Posted 2 days ago »</div>
        </div>
      </article>
    </div>
  </div>
</section>

<footer class="footer">
  <div class="wrap">
    <div class="col-badge">
      <div class="badge"></div>
      <div class="socials"><span></span><span></span><span></span><span></span><span></span></div>
    </div>
    <div class="col-links">
      <h5>Quick Link</h5>
      <ul>
        <li>› Home</li>
        <li>› About Us</li>
        <li>› Services</li>
        <li>› Blog</li>
        <li>› News</li>
        <li>› Contact Us</li>
      </ul>
    </div>
    <div class="col-contact">
      <h5>Contact Us</h5>
      <ul>
        <li><svg width="10" height="14" viewBox="0 0 10 14"><path d="M5 13C2 9 1 7 1 5a4 4 0 0 1 8 0c0 2-1 4-4 8Z" fill="none" stroke="#cfe0ef"/></svg><span>Guardline,<br>2nd Floor, 48 Harbour Road,<br>Eastvale</span></li>
        <li><svg width="10" height="14" viewBox="0 0 10 14"><rect x="1" y="1" width="8" height="12" rx="1.5" fill="none" stroke="#cfe0ef"/></svg><span>Help : 1 800 555 0142</span></li>
        <li><svg width="12" height="10" viewBox="0 0 12 10"><rect x="0.5" y="0.5" width="11" height="9" fill="none" stroke="#cfe0ef"/><path d="M0.5 0.5 6 5 11.5 0.5" fill="none" stroke="#cfe0ef"/></svg><span>Mail : www.guardline.example</span></li>
      </ul>
    </div>
    <div class="col-form">
      <h5>Contact Form</h5>
      <div class="form-row"><div class="field">Name</div><div class="field">Phone</div></div>
      <div class="form-row"><div class="field area">Message</div></div>
      <span class="submit">Send Message</span>
    </div>
  </div>
</footer>

<div class="bottom">
  <div class="wrap">© 2016 Guardline. All Rights Reserved.</div>
</div>

</body>
</html>
```